Q7R Electrical Systems Inc Business Cards

Target Market(s)

Customers

Industry/Entity Type

Construction - Electrical

Contact Information for Business Card

Company Name, Address, Phone, and email address

Font styles to use
Sans Serif

Colors
0054AA
0677BA
7BADD7
CADEEF
E8F1F8

Requirements
Must have
• we would like to use the same design that we had our vehicles wrapped
Nice to have
• The design that we used on our trucks

```html
<!DOCTYPE html>
<html lang="en">
<head>
<meta charset="utf-8">
<title>Q7R Electrical Systems Inc – Business Cards</title>
<link href="https://fonts.googleapis.com/css2?family=Poppins:wght@400;500;600&display=swap" rel="stylesheet">
<style>
  :root {
    --navy: #1b2264;
    --navy-light: #2e3a86;
    --sky: #7badd7;
    --sky-pale: #cadeef;
    --paper: #ffffff;
    --paper-shade: #eef2f7;
    --stage: #e6e9ee;
  }
  * { margin: 0; padding: 0; box-sizing: border-box; }
  html, body {
    width: 1200px; height: 780px; overflow: hidden;
    background: var(--stage);
    font-family: "Poppins", sans-serif;
  }
  .sheet {
    position: relative; width: 1200px; height: 780px;
    display: flex; align-items: center; justify-content: center; gap: 40px;
  }
  .card {
    position: relative; width: 520px; height: 298px;
    border-radius: 16px; overflow: hidden;
    background: linear-gradient(160deg, var(--paper) 0%, var(--paper-shade) 100%);
    box-shadow: 0 10px 28px rgba(20, 30, 70, 0.18);
  }
  .card-shape { position: absolute; inset: 0; width: 100%; height: 100%; }
  .contact-side {
    position: absolute; left: 34px; top: 38px; width: 230px; color: var(--paper);
  }
  .person-name {
    font-weight: 600; font-size: 21px; letter-spacing: 0.5px; line-height: 1.1;
  }
  .person-role {
    font-weight: 400; font-size: 12px; letter-spacing: 1px;
    color: var(--sky); margin-top: 3px;
  }
  .address {
    margin-top: 42px; font-size: 12.5px; line-height: 1.45;
  }
  .contact-line {
    display: flex; align-items: center; gap: 8px;
    font-size: 12.5px; margin-top: 8px;
  }
  .contact-line:first-of-type { margin-top: 14px; }
  .contact-icon { width: 17px; height: 17px; flex: none; }
  .brand-side {
    position: absolute; right: 28px; top: 0; bottom: 0; width: 210px;
    display: flex; align-items: center; justify-content: center;
  }
  .brand-name {
    color: var(--navy); font-weight: 500; font-size: 22px;
    line-height: 1.25; letter-spacing: 0.5px; text-align: left;
  }
  .card-back { display: flex; align-items: center; justify-content: center; }
  .card-back .brand-name { font-size: 30px; text-align: center; }
</style>
</head>
<body>
<main class="sheet">

  <section class="card card-front" aria-label="Business card front">
    <svg class="card-shape" viewBox="0 0 520 298" preserveAspectRatio="none" aria-hidden="true">
      <defs>
        <linearGradient id="navyPanel" x1="0" y1="0" x2="1" y2="1">
          <stop offset="0" stop-color="#161c58"/>
          <stop offset="0.55" stop-color="#2a3580"/>
          <stop offset="1" stop-color="#1b2264"/>
        </linearGradient>
      </defs>
      <path d="M0 0 H282 Q318 150 268 298 H0 Z" fill="url(#navyPanel)"/>
      <path d="M282 0 Q318 150 268 298" fill="none" stroke="#7badd7" stroke-width="3" transform="translate(6 0)"/>
    </svg>

    <div class="contact-side">
      <p class="person-name">DANA L CARVER</p>
      <p class="person-role">MANAGER</p>
      <p class="address">412 Harbor Pine Way # 208<br>Lakeview Springs, FL 32790</p>
      <p class="contact-line">
        <svg class="contact-icon" viewBox="0 0 18 18" aria-hidden="true">
          <circle cx="9" cy="9" r="9" fill="#cadeef"/>
          <rect x="6" y="4" width="6" height="10" rx="1.2" fill="none" stroke="#1b2264" stroke-width="1.3"/>
        </svg>
        407-555-0148
      </p>
      <p class="contact-line">
        <svg class="contact-icon" viewBox="0 0 18 18" aria-hidden="true">
          <circle cx="9" cy="9" r="9" fill="#cadeef"/>
          <rect x="4.5" y="5.5" width="9" height="7" fill="none" stroke="#1b2264" stroke-width="1.2"/>
          <path d="M4.5 5.5 L9 9.5 L13.5 5.5" fill="none" stroke="#1b2264" stroke-width="1.2"/>
        </svg>
        info@q7relectric.com
      </p>
    </div>

    <div class="brand-side">
      <p class="brand-name">Q7R Electrical<br>Systems Inc</p>
    </div>
  </section>

  <section class="card card-back" aria-label="Business card back">
    <p class="brand-name">Q7R Electrical<br>Systems Inc</p>
  </section>

</main>
</body>
</html>
```